Harbor Business Cards

I need a business card designed with the following information.

Company Name: Harbor Wealth Management
Name: BriAnne Dockery
Title: Executive Assistant
Cell: (281) 555-0173
Direct Line: (832) 555-0148
Email: brianne@harborwmx.com
Address: 20537 W. Marlowe PKWY Ste. B
Tomball, TX 77390

I have attached the logo.
I would like it in navy blue and silver.
Thanks.

```html
<!DOCTYPE html>
<html lang="en">
<head>
<meta charset="utf-8">
<title>Harbor Wealth Management – Business Card</title>
<link rel="stylesheet" href="https://fonts.googleapis.com/css2?family=Open+Sans:wght@400;700&display=swap">
<style>
  :root {
    --navy: #2b3389;
    --silver-light: #f2f3f5;
    --silver-mid: #c3c6cc;
    --silver-dark: #9ea2aa;
    --ink-light: #ffffff;
    --text-soft: #e3e5f0;
    --backdrop: #e8e5e1;
  }
  * { box-sizing: border-box; margin: 0; padding: 0; }
  html, body {
    width: 1200px;
    height: 1200px;
    overflow: hidden;
    background: var(--backdrop);
    font-family: "Open Sans", Arial, sans-serif;
  }
  .card {
    position: absolute;
    left: 250px;
    width: 700px;
    height: 400px;
    background: var(--navy);
    overflow: hidden;
  }
  .card--front { top: 152px; }
  .card--back { top: 645px; }

  /* Front */
  .brand {
    position: absolute;
    left: 0;
    right: 0;
    top: 215px;
    display: flex;
    flex-direction: column;
    align-items: center;
    gap: 26px;
  }
  .brand__mark {
    width: 54px;
    height: 54px;
    background: linear-gradient(90deg, var(--silver-dark), var(--silver-light) 50%, var(--silver-mid));
  }
  .brand__name {
    color: var(--silver-mid);
    font-weight: 400;
    font-size: 24px;
    letter-spacing: 8px;
    text-transform: uppercase;
  }

  /* Back */
  .contact {
    position: absolute;
    left: 44px;
    top: 136px;
    color: var(--text-soft);
  }
  .contact__name {
    color: var(--ink-light);
    font-weight: 700;
    font-size: 25px;
    line-height: 30px;
  }
  .contact__title {
    font-size: 16px;
    line-height: 22px;
  }
  .contact__list {
    list-style: none;
    margin-top: 30px;
  }
  .contact__item {
    display: flex;
    align-items: center;
    gap: 12px;
    font-size: 16.5px;
    line-height: 24px;
  }
  .contact__icon {
    width: 19px;
    height: 19px;
    fill: var(--ink-light);
    flex: none;
  }
  .contact__address {
    margin-top: 17px;
    font-size: 16.5px;
    line-height: 24px;
    font-style: normal;
  }
  .corner-mark {
    position: absolute;
    right: -60px;
    bottom: -60px;
    width: 250px;
    height: 250px;
    background: linear-gradient(90deg, var(--silver-dark), var(--silver-light) 45%, var(--silver-mid) 75%, var(--silver-light));
  }
</style>
</head>
<body>
  <section class="card card--front" aria-label="Card front">
    <div class="brand">
      <div class="brand__mark"></div>
      <p class="brand__name">Harbor Wealth Management</p>
    </div>
  </section>

  <section class="card card--back" aria-label="Card back">
    <div class="contact">
      <h1 class="contact__name">BriAnne Dockery</h1>
      <p class="contact__title">Executive Assistant</p>
      <ul class="contact__list">
        <li class="contact__item">
          <svg class="contact__icon" viewBox="0 0 20 20" aria-hidden="true"><path d="M6 1h8a1.5 1.5 0 0 1 1.5 1.5v15A1.5 1.5 0 0 1 14 19H6a1.5 1.5 0 0 1-1.5-1.5v-15A1.5 1.5 0 0 1 6 1zm0.5 2v12h7V3zm3.5 13a1 1 0 1 0 0 2 1 1 0 0 0 0-2z"/></svg>
          <span>(281) 555-0173</span>
        </li>
        <li class="contact__item">
          <svg class="contact__icon" viewBox="0 0 20 20" aria-hidden="true"><path d="M1 6.5C3 3.5 6.5 2.5 10 2.5s7 1 9 4l-1 2.5-3.5-0.8V6.5C13 6 11.5 5.8 10 5.8S7 6 5.5 6.5v1.7L2 9zM6.5 9h7l3 4v4.5h-13V13zm3.5 2a2.2 2.2 0 1 0 0 4.4 2.2 2.2 0 0 0 0-4.4z"/></svg>
          <span>(832) 555-0148</span>
        </li>
        <li class="contact__item">
          <svg class="contact__icon" viewBox="0 0 20 20" aria-hidden="true"><path d="M1 4h18v12H1zm1.8 1.6L10 11l7.2-5.4z"/></svg>
          <span>brianne@harborwmx.com</span>
        </li>
      </ul>
      <address class="contact__address">
        20537 W. Marlowe PKWY Ste. B<br>
        Tomball, TX 77390
      </address>
    </div>
    <div class="corner-mark"></div>
  </section>
</body>
</html>
```